Rapidly growing regional logistics company looking for a modern clean website design.

We need a website for a 5 year old company based in New England.
We offer a complete logistics solution. With services dedicated to the changing economic environment. Services to our customers include, same day delivery, trucking and van service, warehouse & storage, pool distribution, and B2B installations.
We've implemented leading technology along the way, that provides visibility, accountability, up to the minute tracking, and project management.
Our goal to be known in the industry we service as an excellent provider of time-critical services and dependability.
Independently of the services we offer, our customers know that they can count on a true partner.

Target Market(s)

B2B, including printers, retail, manufacturers, wholesalers, electronics, any company that needs product delivered or warehoused

Industry/Entity Type

Logistics

Coding

Coded - Design and coding required

Number of Pages Required

5+ page

Font styles to use
Sans Serif

Colors
0255a3

Requirements
Must have
• Clean, modern design, limited clutter. Limited tabs, preferred everything on 1st screen roll down to see info

```html
<!DOCTYPE html>
<html lang="en">
<head>
<meta charset="utf-8">
<title>Harborline Logistics</title>
<link href="https://fonts.googleapis.com/css2?family=Roboto:wght@300;400;500;700&display=swap" rel="stylesheet">
<style>
:root{
  --brand:#3f67b1;
  --brand-deep:#0255a3;
  --orange:#ff7a00;
  --topbar:#333333;
  --ink:#333333;
  --muted:#777777;
  --navy:#1a2a4a;
  --navy-line:#2c3d5f;
  --panel:#f6f6f6;
  --line:#e2e2e2;
  --white:#ffffff;
}
*{box-sizing:border-box;margin:0;padding:0}
html,body{width:1200px;height:2605px;overflow:hidden}
body{position:relative;font-family:'Roboto',sans-serif;color:var(--ink);background:var(--white)}
.abs{position:absolute}

.topbar{left:0;top:0;width:1200px;height:43px;background:var(--topbar);color:var(--white)}
.topbar .map{left:792px;top:13px;font-size:15px;font-weight:500;white-space:nowrap;line-height:18px}
.topbar .call{left:930px;top:4px;width:160px;font-size:10px;font-weight:500;text-align:center;line-height:11px;white-space:nowrap}
.topbar .phone{left:930px;top:16px;width:160px;font-size:20px;font-weight:500;text-align:center;line-height:22px;white-space:nowrap}

.navbar{left:0;top:43px;width:1200px;height:73px;background:var(--white);border-bottom:1px solid var(--line)}
.brand{left:122px;top:0;width:135px;height:116px;background:var(--white);text-align:center}
.brand .mark{width:70px;height:70px;border-radius:50%;background:var(--brand);margin:4px auto 0}
.brand .name{font-size:15px;font-weight:500;color:var(--brand);letter-spacing:.5px;margin-top:6px;line-height:1}
.nav{left:627px;top:43px;height:73px;display:flex;font-size:14px;font-weight:500;text-transform:uppercase;white-space:nowrap}
.nav a{display:flex;align-items:center;padding:0 17px;color:var(--ink);text-decoration:none;height:73px}
.nav a.active{background:var(--brand);color:var(--white);padding:0 12px}

.hero{left:0;top:116px;width:1200px;height:514px;background:linear-gradient(180deg,#7d5ea8 0%,#b46aa0 22%,#5a4e6e 45%,#3b3b44 70%,#6c6c72 100%)}
.hero-box{left:353px;top:266px;width:493px;height:215px;background:rgba(63,103,177,.82);text-align:center;color:var(--white);padding-top:24px}
.hero-box h1{font-size:38px;font-weight:700;line-height:40px;text-transform:uppercase;white-space:nowrap}
.hero-box p{font-size:16px;line-height:22px;margin-top:8px}
.btn{left:505px;top:450px;width:190px;height:48px;background:var(--orange);color:var(--white);font-size:16px;font-weight:700;display:flex;align-items:center;justify-content:center}

.card{left:122px;width:956px;border:1px solid var(--line);background:var(--white)}
.warehouse{top:676px;height:375px;background:var(--panel)}
.warehouse .photo{left:518px;top:0;width:438px;height:374px;background:linear-gradient(180deg,#c9c3bc,#8a8e98 60%,#b8b3ac)}
.card h2{font-size:34px;font-weight:400;color:var(--brand);white-space:nowrap}
.warehouse h2{left:28px;top:107px}
.warehouse p{left:28px;top:164px;width:460px;font-size:14px;line-height:24px;color:var(--muted)}

.truck{top:1082px;height:373px}
.truck .photo{left:0;top:0;width:437px;height:372px;background:linear-gradient(180deg,#4b6a8e 0%,#d9914a 45%,#a9652f 65%,#2d2d30 100%)}
.truck h2{left:467px;top:45px}
.truck h3{left:467px;top:92px;font-size:20px;font-weight:500;color:#222;white-space:nowrap}
.truck ul{left:467px;top:129px;list-style:none;font-size:12.5px;color:var(--muted);line-height:23px;white-space:nowrap}
.truck li{display:flex;align-items:center;gap:8px}
.truck li svg{flex:none}
.truck .note{left:467px;top:300px;width:340px;font-size:15px;line-height:19px;color:var(--brand)}

.band{left:0;top:1520px;width:1200px;height:288px;background:var(--brand)}
.svc{top:1520px;height:288px;text-align:center;color:var(--white);padding-top:50px}
.svc1{left:122px;width:319px;background:linear-gradient(180deg,#6f86ac,#50679a)}
.svc2{left:441px;width:316px;background:linear-gradient(180deg,#e9e6ec,#ebdccd);color:#555}
.svc3{left:757px;width:321px;background:linear-gradient(180deg,#7592c7,#5a7fc0)}
.svc h4{font-size:19px;font-weight:400;margin-top:14px;white-space:nowrap}
.svc2 h4{color:var(--brand)}
.svc p{font-size:12.5px;line-height:19px;width:270px;margin:8px auto 0}

.t-title{left:0;top:1862px;width:1200px;text-align:center;font-size:33px;font-weight:500;color:#555}
.t-sub{left:0;top:1902px;width:1200px;text-align:center;font-size:14px;color:var(--muted);text-transform:uppercase}
.t-photo{left:122px;top:1922px;width:243px;height:244px;background:linear-gradient(180deg,#d7dbe0,#b8c1cb)}
.t-card{left:309px;top:1948px;width:754px;height:259px;background:var(--white);box-shadow:0 2px 12px rgba(0,0,0,.12);text-align:center;padding-top:40px}
.t-card .name{font-size:15px;font-weight:500;margin-top:10px}
.t-card .role{font-size:12px;color:var(--muted);margin-top:3px}
.t-card .quote{font-size:12.5px;line-height:22px;color:var(--muted);width:640px;margin:24px auto 0}
.dots{left:1078px;top:2052px;display:flex;flex-direction:column;gap:7px}
.dots span{width:10px;height:10px;border-radius:50%;border:1px solid #bbb}
.dots span.on{background:#e5323e;border-color:#e5323e}

.footer{left:0;top:2297px;width:1200px;height:308px;background:var(--navy);color:var(--white)}
.fcol{top:52px;white-space:nowrap}
.fcol h5{font-size:26px;font-weight:400;text-transform:uppercase;margin-bottom:16px}
.fcol a{display:block;color:var(--white);text-decoration:none;font-size:16px;line-height:33px;text-transform:uppercase}
.signup{left:764px;top:110px;display:flex}
.signup .email{width:195px;height:42px;background:var(--white);color:#555;font-size:13px;display:flex;align-items:center;padding-left:12px}
.signup .go{width:111px;height:42px;background:var(--orange);font-size:18px;font-weight:500;display:flex;align-items:center;justify-content:center}
.socials{left:764px;top:175px;display:flex;gap:8px}
.socials span{width:32px;height:32px;border-radius:50%;border:2px solid var(--white)}
.rule{left:0;top:242px;width:1200px;height:1px;background:var(--navy-line)}
.copy{left:126px;top:275px;font-size:13px;white-space:nowrap}
.copy b{color:var(--orange);font-weight:400}
.chat{left:750px;top:268px;width:320px;height:40px;background:#2d4f86;display:flex;align-items:center;justify-content:space-between;padding:0 12px;font-size:14px}
</style>
</head>
<body>

<div class="abs topbar">
  <div class="abs map">FIND US ON MAP</div>
  <div class="abs call">CALL US NOW</div>
  <div class="abs phone">0800-555-0142</div>
</div>

<div class="abs navbar"></div>
<div class="abs brand">
  <div class="mark"></div>
  <div class="name">HARBORLINE</div>
</div>
<nav class="abs nav">
  <a class="active" href="#">Services</a>
  <a href="#">About Us</a>
  <a href="#">Warehouse</a>
  <a href="#">Contact</a>
  <a href="#">Blog</a>
</nav>

<section class="abs hero" role="img" aria-label="Cargo port cranes at sunset beside a highway with a moving freight truck"></section>
<div class="abs hero-box">
  <h1>Welcome to<br>Harborline Logistics</h1>
  <p>Our company was founded in 2012 but our team is seasoned,<br>with a combined 75 years of experience.</p>
</div>
<div class="abs btn">LEARN MORE</div>

<section class="abs card warehouse">
  <h2 class="abs">Warehousing</h2>
  <p class="abs">Our warehouse facility may prove to be one of the most valuable extensions of your company's operations. With a secure warehouse conveniently located in central New England to supplement your firm's storage and distribution needs.</p>
  <div class="abs photo" role="img" aria-label="Warehouse aisle with tall stocked shelving and workers walking"></div>
</section>

<section class="abs card truck">
  <div class="abs photo" role="img" aria-label="White delivery truck on a road at sunset"></div>
  <h2 class="abs">Truck &amp; Van Service</h2>
  <h3 class="abs">Trucking, vehicle and ground transportation include:</h3>
  <ul class="abs">
    <li><svg width="10" height="10" viewBox="0 0 10 10"><circle cx="5" cy="5" r="4.3" fill="none" stroke="#3f67b1"/><path d="M4 3l2 2-2 2" fill="none" stroke="#3f67b1"/></svg>Rush and pre-scheduled delivery</li>
    <li><svg width="10" height="10" viewBox="0 0 10 10"><circle cx="5" cy="5" r="4.3" fill="none" stroke="#3f67b1"/><path d="M4 3l2 2-2 2" fill="none" stroke="#3f67b1"/></svg>Light and heavy trucking (cargo vans to liftgates)</li>
    <li><svg width="10" height="10" viewBox="0 0 10 10"><circle cx="5" cy="5" r="4.3" fill="none" stroke="#3f67b1"/><path d="M4 3l2 2-2 2" fill="none" stroke="#3f67b1"/></svg>Line haul from pick up locations to airports and other designated locations</li>
    <li><svg width="10" height="10" viewBox="0 0 10 10"><circle cx="5" cy="5" r="4.3" fill="none" stroke="#3f67b1"/><path d="M4 3l2 2-2 2" fill="none" stroke="#3f67b1"/></svg>Expedited ground services</li>
    <li><svg width="10" height="10" viewBox="0 0 10 10"><circle cx="5" cy="5" r="4.3" fill="none" stroke="#3f67b1"/><path d="M4 3l2 2-2 2" fill="none" stroke="#3f67b1"/></svg>LTL (Less than Truckload)</li>
    <li><svg width="10" height="10" viewBox="0 0 10 10"><circle cx="5" cy="5" r="4.3" fill="none" stroke="#3f67b1"/><path d="M4 3l2 2-2 2" fill="none" stroke="#3f67b1"/></svg>Late-night delivery — we are open 24 hours per day, 365 days per year</li>
    <li><svg width="10" height="10" viewBox="0 0 10 10"><circle cx="5" cy="5" r="4.3" fill="none" stroke="#3f67b1"/><path d="M4 3l2 2-2 2" fill="none" stroke="#3f67b1"/></svg>Truckload</li>
  </ul>
  <p class="abs note">Not everything you ship needs a truck for smaller shipments we offer van service</p>
</section>

<div class="abs band"></div>
<div class="abs svc svc1" role="img" aria-label="Forklift loading pallets in a distribution centre">
  <svg width="60" height="80" viewBox="0 0 60 80" fill="none" stroke="#fff" stroke-width="4"><path d="M30 50V8M30 8l-8 8M30 8l8 8M30 36L10 20M10 20v10M10 20h10M30 36L50 20M50 20v10M50 20H40"/><circle cx="30" cy="60" r="9"/></svg>
  <h4>Distribution &amp; Pool Services</h4>
  <p>Pool Distribution is the distribution of product to numerous customers within a particular geographic region.</p>
</div>
<div class="abs svc svc2" role="img" aria-label="Courier handing over a cardboard parcel">
  <svg width="80" height="80" viewBox="0 0 80 80" fill="none" stroke="#3f67b1" stroke-width="4" stroke-linejoin="round"><path d="M10 24L40 10l30 14v34L40 72 10 58z" fill="#fff"/><path d="M10 24l30 14 30-14M40 38v34M24 17l30 14v12"/></svg>
  <h4>Same-day Delivery Service</h4>
  <p>Regardless of the specifics of your needs, HARBORLINE can handle your same-day delivery needs.</p>
</div>
<div class="abs svc svc3" role="img" aria-label="Delivery driver handing a package to a customer at the door">
  <svg width="100" height="80" viewBox="0 0 100 80" fill="none" stroke="#fff" stroke-width="4" stroke-linejoin="round"><path d="M8 14h52v42H8z"/><path d="M60 28h18l12 14v14H60z"/><circle cx="24" cy="62" r="7" fill="#5a7fc0"/><circle cx="76" cy="62" r="7" fill="#5a7fc0"/><path d="M22 26l8 9-8 9M34 26l8 9-8 9"/></svg>
  <h4>Dedicated Delivery Service</h4>
  <p>Our goal is to make the process easy, and of course, to make you look good in the eyes of your customers and suppliers.</p>
</div>

<div class="abs t-title">TESTIMONIAL</div>
<div class="abs t-sub">Customer say what</div>
<div class="abs t-photo" role="img" aria-label="Portrait of a smiling client in a light blue shirt"></div>
<div class="abs t-card">
  <svg width="42" height="38" viewBox="0 0 42 38"><path d="M21 2C10 2 2 9 2 17c0 5 3 9 7 12l-3 8 10-5c2 .5 3 .5 5 .5 11 0 19-7 19-15.5S32 2 21 2z" fill="#2f4b6e"/><path d="M12 14h18M12 20h14" stroke="#fff" stroke-width="2.5"/></svg>
  <div class="name">Owen Hartley</div>
  <div class="role">Director at Northway Bank</div>
  <p class="quote">In case you needed something fun and pointless Bacon questioned the Aristotelian concepts of formal cause and final cause, and promoted the idea that science should study the laws of "simple" natures, such as heat, rather than assuming that there is any specific</p>
</div>
<div class="abs dots"><span></span><span></span><span class="on"></span></div>

<footer class="abs footer">
  <div class="abs fcol" style="left:125px"><h5>Our Info</h5><a href="#">Homepage</a><a href="#">About Us</a><a href="#">Hiring</a></div>
  <div class="abs fcol" style="left:304px"><h5>Booking</h5><a href="#">Booking Page</a><a href="#">Blog</a></div>
  <div class="abs fcol" style="left:478px"><h5>Additional Links</h5><a href="#">Gift Card</a><a href="#">Help</a><a href="#">We're Green</a></div>
  <div class="abs fcol" style="left:764px"><h5>Stay Connected</h5></div>
  <div class="abs signup"><div class="email">EMAIL</div><div class="go">SIGN UP</div></div>
  <div class="abs socials"><span></span><span></span><span></span><span></span></div>
  <div class="abs rule"></div>
  <div class="abs copy">Copyright <b>Harborline Logistics</b> @2017</div>
  <div class="abs chat"><span>Live Chat</span><span>⌄ &nbsp;+</span></div>
</footer>

</body>
</html>
```